Fabric Softener

We need fabric softener. Bottle picture attached for reference. Color of bottle can be proposed as well. Normally bottle is pink and blue color

Logo is also attached that shall be used.
Updates

Need extra days to review

Low designer entries

Target Market(s)

Niche

Font styles to use
Sans Serif

Requirements
Must have
• Fabric, Brightness, Nature
Nice to have
• Good colors
Should not have
• Adults

```html
<!DOCTYPE html>
<html lang="en">
<head>
<meta charset="utf-8">
<title>Brisa Super Softener – Fabric Conditioner</title>
<link rel="stylesheet" href="https://fonts.googleapis.com/css2?family=Roboto+Condensed:wght@400;700;900&family=Great+Vibes&display=swap">
<style>
  :root{
    --bg:#ffffff;
    --bottle:#2a8fd6;
    --bottle-shade:#2377b8;
    --cap:#eef0f2;
    --cap-shade:#d9dde1;
    --label-top:#d6ecfb;
    --label-mid:#8ccdf2;
    --label-low:#5fb8ec;
    --navy:#123a8a;
    --pink:#f27ea3;
    --pink-soft:#f9b7c9;
    --leaf:#a9c9a0;
    --white:#ffffff;
  }
  html,body{margin:0;padding:0;overflow:hidden;background:var(--bg);}
  .canvas{width:1200px;height:1200px;position:relative;overflow:hidden;background:var(--bg);}
  .bottle{position:absolute;inset:0;}
  .headline{font-family:"Roboto Condensed",sans-serif;font-weight:900;fill:var(--navy);stroke:var(--white);stroke-width:5px;paint-order:stroke;}
  .subline{font-family:"Roboto Condensed",sans-serif;font-weight:700;fill:var(--navy);font-size:17px;}
  .brand-name{font-family:"Roboto Condensed",sans-serif;font-weight:700;fill:var(--navy);font-size:48px;}
  .tagline{font-family:"Great Vibes",cursive;fill:var(--navy);font-size:38px;}
  .new-tag{font-family:"Roboto Condensed",sans-serif;font-weight:700;fill:var(--white);font-size:13px;}
  .badge-num{font-family:"Roboto Condensed",sans-serif;font-weight:900;fill:var(--white);font-size:34px;}
  .badge-text{font-family:"Roboto Condensed",sans-serif;font-weight:700;fill:var(--white);font-size:13px;}
  .loads{font-family:"Roboto Condensed",sans-serif;font-weight:700;fill:var(--navy);font-size:17px;}
  .volume{font-family:"Roboto Condensed",sans-serif;font-weight:700;fill:var(--navy);font-size:20px;}
</style>
</head>
<body>
<div class="canvas">
<svg class="bottle" width="1200" height="1200" viewBox="0 0 1200 1200">
  <defs>
    <linearGradient id="bodyShade" x1="0" x2="1" y1="0" y2="0">
      <stop offset="0" stop-color="var(--bottle)"/>
      <stop offset="0.55" stop-color="var(--bottle)"/>
      <stop offset="1" stop-color="var(--bottle-shade)"/>
    </linearGradient>
    <linearGradient id="labelSky" x1="0" x2="0" y1="0" y2="1">
      <stop offset="0" stop-color="var(--label-top)"/>
      <stop offset="0.45" stop-color="var(--label-mid)"/>
      <stop offset="1" stop-color="var(--label-low)"/>
    </linearGradient>
    <linearGradient id="floralTones" x1="0" x2="1" y1="0" y2="1">
      <stop offset="0" stop-color="var(--leaf)" stop-opacity="0.8"/>
      <stop offset="0.5" stop-color="var(--pink-soft)"/>
      <stop offset="1" stop-color="var(--pink)" stop-opacity="0.85"/>
    </linearGradient>
    <clipPath id="labelClip">
      <path d="M392,720 C392,540 470,436 566,436 C660,436 730,520 764,640 L788,900 C792,1010 700,1100 598,1100 C486,1100 398,1010 392,900 Z"/>
    </clipPath>
    <path id="volumeArc" d="M468,1012 Q604,1138 752,1000"/>
  </defs>

  <!-- cap -->
  <rect class="cap" x="532" y="52" width="148" height="108" rx="34" fill="var(--cap)"/>
  <rect class="collar" x="506" y="152" width="196" height="62" rx="6" fill="var(--cap-shade)"/>

  <!-- bottle body -->
  <path class="body" fill="url(#bodyShade)"
        d="M512,212 L698,212 C708,300 760,380 820,470 C868,540 884,620 884,720 L884,1110 C884,1132 870,1144 848,1144 L392,1144 C370,1144 356,1132 356,1110 L356,660 C356,560 400,470 450,400 C490,340 506,280 512,212 Z"/>
  <!-- handle opening -->
  <ellipse class="handle" cx="740" cy="592" rx="50" ry="136" transform="rotate(-22 740 592)" fill="var(--white)"/>

  <!-- label -->
  <g clip-path="url(#labelClip)">
    <rect x="380" y="430" width="420" height="680" fill="url(#labelSky)"/>
    <rect class="floral-art" x="380" y="830" width="420" height="280" fill="url(#floralTones)"
          role="img" aria-label="Watercolour pink roses with green and golden leaves"/>
  </g>

  <!-- brand -->
  <g class="brand">
    <circle cx="438" cy="562" r="9" fill="var(--white)"/>
    <text class="brand-name" x="454" y="580">Brisa</text>
  </g>

  <!-- product name -->
  <g transform="rotate(-6 560 700)">
    <text class="headline" x="444" y="700" font-size="48">SUPER</text>
    <rect x="576" y="647" width="46" height="20" rx="3" fill="var(--pink)"/>
    <text class="new-tag" x="599" y="662" text-anchor="middle">NEW</text>
    <text class="headline" x="400" y="748" font-size="58">SOFTENER</text>
    <text class="subline" x="454" y="772">FABRIC CONDITIONER</text>
  </g>

  <text class="tagline" transform="rotate(-14 560 830)" x="474" y="832">Amazing Shine</text>
  <text class="tagline" transform="rotate(-14 560 860)" x="480" y="872">&amp; Fragrance</text>

  <!-- freshness badge -->
  <path d="M656,924 L788,924 L788,972 L656,972 Q646,972 646,962 L646,934 Q646,924 656,924 Z" fill="var(--pink)" stroke="var(--white)" stroke-width="3"/>
  <text class="badge-num" x="658" y="962">30</text>
  <text class="badge-text" x="702" y="946">DAYS OF</text>
  <text class="badge-text" x="702" y="962">FRESHNESS</text>
  <text class="loads" x="758" y="996" text-anchor="middle">120 LOADS</text>

  <text class="volume"><textPath href="#volumeArc" startOffset="50%" text-anchor="middle">130 FL OZ (1.05 GAL) 3.99L</textPath></text>
</svg>
</div>
</body>
</html>
```